Innovative Consulting Firm Needs New Business Cards and Stationary

Our Innovative Consulting Firm, Larkfield Consulting, is in need of new business cards and stationary designs. We want two-sided cards that incorporate our logo, which is attached. We are looking for something not too formal, but is professional and slick.

Card should have the following information:
Name (ex. Tom Bradley)
Title (ex. Manager)
Address (ex. 24680 Cedar Lane)
Address 2 (ex. Suite 100)
City
State
Zip Code
Mobile
Email

The card should also have our website: www.larkfieldconsulting.example

Industry/Entity Type

Management Consulting

Contact Information for Business Card

Name (ex. Tom Bradley)
Title (ex. Manager)
Address 2 (ex. Suite 100)
City
State
Zip Code
Mobile
Email

Font styles to use
Sans Serif

Requirements
Must have
• The colors on the card must match the colors in the logo. The exact color codes are attached in a pdf.
Nice to have
• The Company's Tagline is "Focused on your Future". This might be nice to incorporate, but not necessary.

```html
<!DOCTYPE html>
<html lang="en">
<head>
<meta charset="utf-8">
<title>Larkfield Consulting – Business Cards</title>
<link href="https://fonts.googleapis.com/css2?family=Jost:wght@300;400;500;600&display=swap" rel="stylesheet">
<style>
  :root {
    --navy: #1f4f7b;
    --gold: #f5ad1b;
    --ink: #3a3a3a;
    --paper: #ffffff;
    --backdrop: #3b2f27;
  }
  * { margin: 0; padding: 0; box-sizing: border-box; }
  html, body {
    width: 1200px;
    height: 1160px;
    overflow: hidden;
    background: var(--backdrop);
    font-family: "Jost", sans-serif;
  }
  .canvas { position: relative; width: 1200px; height: 1160px; }

  .card {
    position: absolute;
    width: 666px;
    height: 381px;
    background: var(--paper);
    border-radius: 17px;
    overflow: hidden;
  }
  .card--front { left: 278px; top: 134px; }
  .card--back  { left: 274px; top: 574px; }

  .brand {
    position: absolute;
    left: 0; right: 0;
    display: flex;
    justify-content: center;
    align-items: center;
    gap: 12px;
  }
  .brand__dot {
    width: 22px; height: 22px;
    border-radius: 50%;
    background: var(--gold);
  }
  .brand__name {
    font-family: "Jost", sans-serif;
    font-weight: 500;
    font-size: 40px;
    color: var(--navy);
    letter-spacing: 0.5px;
    line-height: 1;
  }
  .card--front .brand { top: 54px; }
  .card--back .brand  { top: 157px; }

  .contact {
    position: absolute;
    left: 0; right: 0;
    text-align: center;
    color: var(--ink);
    font-weight: 300;
    font-size: 19px;
    line-height: 1;
  }
  .contact--address { top: 172px; }
  .contact--lines {
    top: 207px;
    display: flex;
    justify-content: center;
    align-items: center;
    gap: 6px;
  }
  .contact__item { display: inline-flex; align-items: center; gap: 6px; }
  .contact__item + .contact__item { margin-left: 18px; }
  .contact__icon { width: 16px; height: 16px; }

  .wave { position: absolute; left: 0; top: 0; width: 666px; height: 381px; }

  .person {
    position: absolute;
    left: 38px;
    top: 306px;
    color: var(--paper);
  }
  .person__name {
    font-size: 29px;
    font-weight: 400;
    letter-spacing: 0.5px;
    line-height: 1;
  }
  .person__title {
    margin-top: 8px;
    font-size: 17px;
    font-weight: 300;
    letter-spacing: 1px;
    line-height: 1;
  }
  .web--front {
    position: absolute;
    right: 44px;
    top: 337px;
    color: var(--paper);
    font-size: 17px;
    font-weight: 600;
    letter-spacing: 0.8px;
    line-height: 1;
  }
  .web--back {
    position: absolute;
    left: 0; right: 0;
    top: 243px;
    text-align: center;
    color: var(--navy);
    font-size: 16px;
    font-weight: 500;
    letter-spacing: 2.6px;
    line-height: 1;
  }
</style>
</head>
<body>
<main class="canvas">

  <section class="card card--front" aria-label="Business card front">
    <svg class="wave" viewBox="0 0 666 381" aria-hidden="true">
      <path fill="var(--navy)" d="M0,279 C120,250 250,262 400,290 C520,312 610,295 666,252 L666,381 L0,381 Z"/>
      <path fill="var(--gold)" d="M390,290 C520,305 615,272 666,210 L666,236 C615,285 520,305 390,290 Z"/>
    </svg>

    <div class="brand">
      <span class="brand__dot"></span>
      <span class="brand__name">Larkfield Consulting</span>
    </div>

    <p class="contact contact--address">24680 Cedar Lane, Suite 100, Cityname, State 00000</p>
    <div class="contact contact--lines">
      <span class="contact__item">
        <svg class="contact__icon" viewBox="0 0 16 16" aria-hidden="true">
          <rect x="4" y="1" width="8" height="14" rx="1.5" fill="var(--gold)"/>
          <rect x="5.5" y="3" width="5" height="4" fill="#fff"/>
        </svg>
        012.345.6789
      </span>
      <span class="contact__item">
        <svg class="contact__icon" viewBox="0 0 16 16" aria-hidden="true">
          <rect x="1" y="4" width="14" height="9" rx="1" fill="var(--gold)"/>
          <path d="M1.5,4.5 L8,9 L14.5,4.5" fill="none" stroke="#fff" stroke-width="1.3"/>
        </svg>
        info@larkfieldconsulting.example
      </span>
    </div>

    <div class="person">
      <p class="person__name">TOM BRADLEY</p>
      <p class="person__title">Manager</p>
    </div>
    <p class="web--front">www.LarkfieldConsulting.example</p>
  </section>

  <section class="card card--back" aria-label="Business card back">
    <div class="brand">
      <span class="brand__dot"></span>
      <span class="brand__name">Larkfield Consulting</span>
    </div>
    <p class="web--back">www.larkfieldconsulting.example</p>
  </section>

</main>
</body>
</html>
```